Delegate Welcome sign

The Copperfield Lodge hotel in Pine Bush NY is welcoming delegations from many different countries during 2019. We want to make a welcome sign about 16:9 ratio about 4 feet high with raised letters. I have attached a background design that we liked and a template with the wording. As you will see I need help with it.

```html
<!DOCTYPE html>
<html lang="en">
<head>
<meta charset="utf-8">
<title>Delegate Welcome Sign – The Copperfield Lodge Hotel</title>
<link rel="stylesheet" href="https://fonts.googleapis.com/css2?family=Montserrat:wght@600;700;800&display=swap">
<style>
  :root {
    --forest: #26352f;
    --forest-light: #2e4039;
    --forest-dark: #1f2c27;
    --gold: #f8bd3a;
    --white: #ffffff;
    --shadow: rgba(0, 0, 0, 0.55);
  }
  html, body {
    margin: 0;
    padding: 0;
    width: 1200px;
    height: 675px;
    overflow: hidden;
    background: var(--forest);
  }
  .sign {
    position: relative;
    width: 1200px;
    height: 675px;
    overflow: hidden;
    font-family: "Montserrat", Arial, sans-serif;
    text-align: center;
  }
  .sign__backdrop {
    position: absolute;
    inset: 0;
    background: radial-gradient(ellipse at 50% 45%, var(--forest-light) 0%, var(--forest) 55%, var(--forest-dark) 100%);
  }
  .line {
    position: absolute;
    left: 0;
    width: 100%;
    margin: 0;
    line-height: 1;
    transform: translateY(-50%);
  }
  .hotel-name {
    top: 83px;
    font-size: 41px;
    font-weight: 800;
    letter-spacing: 1px;
    color: var(--gold);
  }
  .welcomes {
    top: 156px;
    font-size: 41px;
    font-weight: 600;
    color: var(--gold);
  }
  .frame {
    position: absolute;
    left: 0;
    top: 0;
  }
  .frame path {
    fill: none;
    stroke: var(--gold);
    stroke-width: 3;
  }
  .headline {
    font-size: 77px;
    font-weight: 700;
    letter-spacing: 1px;
    color: var(--white);
    text-shadow: 4px 5px 8px var(--shadow);
  }
  .headline--one { top: 259px; }
  .headline--two { top: 352px; }
  .subline {
    font-size: 47px;
    font-weight: 700;
    letter-spacing: 1.5px;
    color: var(--white);
    text-shadow: 3px 4px 6px var(--shadow);
  }
  .subline--one { top: 440px; }
  .subline--two { top: 500px; }
  .hashtag {
    top: 608px;
    font-size: 38px;
    font-weight: 600;
    color: var(--gold);
  }
</style>
</head>
<body>
<main class="sign">
  <div class="sign__backdrop" role="img" aria-label="Dark green background with a dense pattern of tonal leaves and vines"></div>

  <p class="line hotel-name">THE COPPERFIELD LODGE HOTEL</p>
  <p class="line welcomes">welcomes</p>

  <svg class="frame" width="1200" height="675" viewBox="0 0 1200 675" aria-hidden="true">
    <path d="M430 160 H79 V557 H1122 V160 H772"/>
  </svg>

  <h1 class="line headline headline--one">2019 INTERNATIONAL</h1>
  <p class="line headline headline--two">DELEGATES</p>
  <p class="line subline subline--one">TO THE HUDSON VALLEY</p>
  <p class="line subline subline--two">IN NEW YORK</p>

  <p class="line hashtag">#copperfieldlodgehotel</p>
</main>
</body>
</html>
```